We use a logo that is a sort of smiley face. The mouth is a wrench curved to make the smile. One end of the wrench is a box end and the other is an open end. (These are types of wrenches. If you google combination wrench it will show you) The for the eyes they are hex shaped like nuts (six sides). We want to use this logo and our information for a letterhead that we will use to print invoices. The top right corner needs to have a clean area for the invoice number.
Steadfield Automotive Repair
and Maintenance
48307 Talmin Dr.
Austin, TX 78729
512-608-4197
www.steadfieldautofix.example
If you can design this information plus the smiley face on there somewhere.
Automotive
Steadfield Automotive Repair and Maintenance

```html
<!DOCTYPE html>
<html lang="en">
<head>
<meta charset="utf-8">
<title>Steadfield Automotive Repair and Maintenance – Invoice Letterhead</title>
<link rel="stylesheet" href="https://fonts.googleapis.com/css2?family=Didact+Gothic&display=swap">
<style>
  :root {
    --backdrop: #e9e4dc;
    --paper: #ffffff;
    --ink: #111111;
    --band: #000000;
    --invoice-field: #fffac8;
  }
  * { box-sizing: border-box; margin: 0; padding: 0; }
  html, body {
    width: 1200px;
    height: 960px;
    overflow: hidden;
    background: var(--backdrop);
  }
  .letterhead {
    position: absolute;
    left: 50px;
    top: 145px;
    width: 1100px;
    height: 669px;
    font-family: "Didact Gothic", "Century Gothic", sans-serif;
    color: var(--ink);
  }
  .sheet-shape {
    position: absolute;
    inset: 0;
    width: 1100px;
    height: 669px;
  }
  .brand-name {
    position: absolute;
    left: 64px;
    top: 52px;
    line-height: 1;
  }
  .brand-name .name-main {
    display: block;
    font-size: 52px;
    letter-spacing: 1px;
  }
  .brand-name .name-sub {
    display: block;
    margin-top: 8px;
    font-size: 15px;
    letter-spacing: 0.5px;
  }
  .contact-line {
    position: absolute;
    left: 64px;
    top: 146px;
    font-size: 16px;
    white-space: nowrap;
  }
  .contact-line .sep {
    margin: 0 10px;
  }
  .center-mark {
    position: absolute;
    left: 596px;
    top: 62px;
    display: flex;
    align-items: center;
    gap: 10px;
    font-size: 22px;
  }
  .center-mark .mark-dot {
    width: 40px;
    height: 40px;
    border: 3px solid var(--ink);
    border-radius: 50%;
  }
  .invoice-number-field {
    position: absolute;
    left: 840px;
    top: 21px;
    width: 237px;
    height: 64px;
    background: var(--invoice-field);
  }
</style>
</head>
<body>
  <main class="letterhead">
    <svg class="sheet-shape" viewBox="0 0 1100 669" aria-hidden="true">
      <path d="M0,0 H1100 V604 H0 Z" fill="var(--paper)"/>
      <path class="footer-band" d="M0,604 H1100 V669 Q550,543 0,669 Z" fill="var(--band)"/>
    </svg>

    <header>
      <h1 class="brand-name">
        <span class="name-main">STEADFIELD</span>
        <span class="name-sub">AUTOMOTIVE REPAIR AND MAINTENANCE</span>
      </h1>

      <p class="contact-line">
        48307 Talmin Dr. Austin, TX<span class="sep">•</span>78729 512-608-4197<span class="sep">•</span>www.steadfieldautofix.example
      </p>

      <div class="center-mark">
        <span class="mark-dot"></span>
        <span class="mark-name">Steadfield</span>
      </div>

      <div class="invoice-number-field" aria-label="Invoice number area"></div>
    </header>
  </main>
</body>
</html>
```